KLV Business Card - Courier/Transportation - Needs Double Sided Business Card

I am searching for business cards for my company. Currently I just need cards for the (3) founders.

We are a new courier/transporation company that specializes in the medical/pharmaceutical arena.

As you will see from our logo, our primary colors are green and black. We strive to have an efficient, streamlined service offering. I like traditional looks, but also want to showcase our young, modern feel. I would like our card to be double sided.

Target Market(s)

Pharmacies
Hospitals
Physcian Office
Labs

Industry/Entity Type

Business

```html
<!DOCTYPE html>
<html lang="en">
<head>
<meta charset="utf-8">
<title>KLV Courier Business Card</title>
<link rel="stylesheet" href="https://fonts.googleapis.com/css2?family=Open+Sans:wght@400;600&display=swap">
<style>
  :root {
    --page-bg: #ecebe8;
    --card-white: #ffffff;
    --card-dark-top: #242424;
    --card-dark-bottom: #3b3b3b;
    --brand-green: #3cb54a;
    --text-dark: #1f1f1f;
    --text-mid: #333333;
    --shadow: rgba(0, 0, 0, 0.28);
  }
  * { margin: 0; padding: 0; box-sizing: border-box; }
  html, body { width: 1200px; height: 1000px; overflow: hidden; }
  body {
    background: var(--page-bg);
    font-family: "Open Sans", Arial, sans-serif;
    position: relative;
  }
  .card {
    position: absolute;
    width: 620px;
    height: 354px;
    border-radius: 3px;
    box-shadow: 0 6px 18px var(--shadow);
  }
  .card--front {
    left: 150px;
    top: 110px;
    background: var(--card-white);
  }
  .card--back {
    left: 470px;
    top: 510px;
    background: linear-gradient(180deg, var(--card-dark-top), var(--card-dark-bottom));
    display: flex;
    align-items: center;
    justify-content: center;
  }
  .wordmark {
    color: var(--brand-green);
    font-weight: 600;
    letter-spacing: 4px;
    line-height: 1;
    white-space: nowrap;
  }
  .card--front .wordmark {
    position: absolute;
    right: 40px;
    top: 44px;
    font-size: 40px;
  }
  .card--back .wordmark { font-size: 58px; }
  .address {
    position: absolute;
    right: 40px;
    top: 104px;
    text-align: right;
    color: var(--brand-green);
    font-size: 17px;
    line-height: 1.3;
  }
  .holder {
    position: absolute;
    left: 60px;
    top: 212px;
    color: var(--text-dark);
  }
  .holder__name { font-size: 25px; line-height: 1.1; }
  .holder__role { font-size: 15px; margin-top: 4px; }
  .contact {
    position: absolute;
    left: 60px;
    bottom: 28px;
    list-style: none;
    font-size: 19px;
    color: var(--text-dark);
  }
  .contact__item { display: flex; align-items: center; gap: 10px; height: 30px; }
  .contact__icon { width: 24px; height: 22px; fill: var(--text-dark); }
  .website {
    position: absolute;
    right: 40px;
    bottom: 36px;
    font-size: 17px;
    color: var(--text-mid);
  }
</style>
</head>
<body>
  <section class="card card--front" aria-label="Business card front">
    <div class="wordmark">KLV COURIER</div>
    <address class="address" style="font-style:normal">
      KLV Courier<br>
      2480 Meadow Ridge Dr,<br>
      Carmel,<br>
      IN 46032
    </address>
    <div class="holder">
      <div class="holder__name">Mr.Smith</div>
      <div class="holder__role">Director</div>
    </div>
    <ul class="contact">
      <li class="contact__item">
        <svg class="contact__icon" viewBox="0 0 24 24" aria-hidden="true"><path d="M6.6 10.8a15.1 15.1 0 0 0 6.6 6.6l2.2-2.2c.3-.3.7-.4 1-.2 1.1.4 2.3.6 3.6.6.6 0 1 .4 1 1V20c0 .6-.4 1-1 1A17 17 0 0 1 3 4c0-.6.4-1 1-1h3.5c.6 0 1 .4 1 1 0 1.3.2 2.5.6 3.6.1.3 0 .7-.2 1z"/></svg>
        <span>000-00000000</span>
      </li>
      <li class="contact__item">
        <svg class="contact__icon" viewBox="0 0 24 20" aria-hidden="true"><path d="M1 2h22v16H1z" fill="none" stroke="#1f1f1f" stroke-width="2"/><path d="M1 2l11 9 11-9" fill="none" stroke="#1f1f1f" stroke-width="2"/></svg>
        <span>hello@klvcourier.net</span>
      </li>
    </ul>
    <div class="website">www.KLVcourier.net</div>
  </section>

  <section class="card card--back" aria-label="Business card back">
    <div class="wordmark">KLV COURIER</div>
  </section>
</body>
</html>
```